Bright Harbor Coverage Partners
Auto-Home-Health-Business
Project: Bright Harbor Coverage Partners
Bright Harbor Coverage Partners - Consulting
Creative Brief
Professional
Dario F Menzel
Insurance Broker
4287 Willowgate Pkwy, suite D Fairmont Springs,CA,91458
mtorvel@bhcpins.com
0K52718
I need to more sets of business cards for my partners
I would like the logo

```html
<!DOCTYPE html>
<html lang="en">
<head>
<meta charset="utf-8">
<title>Bright Harbor Coverage Partners – Business Cards</title>
<link rel="stylesheet" href="https://fonts.googleapis.com/css2?family=Open+Sans:ital,wght@0,400;0,600;1,400;1,700&display=swap">
<style>
  :root {
    --stage: #3b3b3b;
    --paper: #ffffff;
    --brand-blue: #2d5f96;
    --band-dark: #0f2f5c;
    --band-mid: #1f5593;
    --band-light: #3f7fc0;
    --ink: #333333;
    --rule: #c9ced6;
  }
  * { margin: 0; padding: 0; box-sizing: border-box; }
  html, body { width: 1200px; height: 698px; overflow: hidden; background: var(--stage); }
  .stage { position: relative; width: 1200px; height: 698px; background: var(--stage); }

  .card {
    position: absolute;
    border-radius: 22px;
    overflow: hidden;
    background: var(--paper);
    box-shadow: 0 2px 6px rgba(0,0,0,0.35);
  }
  .card--front { left: 72px; top: 67px; width: 458px; height: 257px; }
  .card--back-light { left: 655px; top: 67px; width: 461px; height: 255px; }
  .card--back-dark {
    left: 362px; top: 384px; width: 454px; height: 259px;
    background: radial-gradient(ellipse at 50% 35%, #3f7fc0 0%, #1d4f8c 55%, #0d2a55 100%);
  }

  /* Brand lockup: plain name beside a plain square */
  .brand {
    position: absolute; left: 0; right: 0;
    display: flex; align-items: center; justify-content: center; gap: 12px;
    transform: translateY(-50%);
  }
  .brand__square { width: 30px; height: 30px; background: var(--brand-blue); flex: none; }
  .brand__name {
    font-family: "Open Sans", sans-serif; font-weight: 600;
    font-size: 21px; line-height: 1.15; color: var(--brand-blue);
  }
  .brand--on-dark .brand__square { background: #ffffff; }
  .brand--on-dark .brand__name { color: #ffffff; font-size: 23px; }

  .card--front .brand { top: 65px; }
  .card--back-light .brand { top: 101px; }
  .card--back-dark .brand { top: 127px; }

  /* Front band */
  .name-band {
    position: absolute; left: 0; right: 0; top: 146px; height: 32px;
    background: linear-gradient(180deg, var(--band-mid) 0%, var(--band-dark) 100%);
    display: flex; align-items: center; gap: 10px;
    padding-left: 108px; color: #ffffff; font-family: "Open Sans", sans-serif;
  }
  .name-band__name { font-style: italic; font-weight: 700; font-size: 13px; }
  .name-band__title { font-size: 8.5px; font-style: italic; }

  .contact {
    position: absolute; left: 0; right: 0;
    font-family: "Open Sans", sans-serif; font-size: 9px; color: var(--ink);
    display: flex; align-items: center; justify-content: center; gap: 9px; white-space: nowrap;
  }
  .contact--lines { top: 196px; }
  .contact--address { top: 217px; }
  .contact--licence { top: 237px; }
  .contact__item { display: inline-flex; align-items: center; gap: 3px; }
  .contact__item svg { width: 8px; height: 8px; fill: var(--ink); }

  /* Back band */
  .back-rule { position: absolute; left: 0; right: 0; top: 197px; height: 1px; background: var(--rule); }
  .back-band {
    position: absolute; left: 0; right: 0; top: 209px; height: 29px;
    background: linear-gradient(90deg, var(--band-dark) 0%, var(--band-mid) 45%, var(--band-light) 100%);
  }
</style>
</head>
<body>
<main class="stage">

  <section class="card card--front">
    <div class="brand">
      <span class="brand__square"></span>
      <span class="brand__name">Bright Harbor<br>Coverage Partners</span>
    </div>

    <div class="name-band">
      <span class="name-band__name">Dario F Menzel,</span>
      <span class="name-band__title">Insurance Broker</span>
    </div>

    <div class="contact contact--lines">
      <span class="contact__item">
        <svg viewBox="0 0 10 10"><path d="M2 0.5 L3.8 2.3 L2.8 3.5 C3.5 5 5 6.5 6.5 7.2 L7.7 6.2 L9.5 8 L8 9.5 C4 9 1 6 0.5 2 Z"/></svg>
        (555)214-3860
      </span>
      <span class="contact__item">
        <svg viewBox="0 0 10 10"><rect x="2.5" y="0.5" width="5" height="9" rx="1"/></svg>
        (555)307-4192
      </span>
      <span class="contact__item">
        <svg viewBox="0 0 10 10"><rect x="0.5" y="3" width="9" height="5" rx="1"/><rect x="2.5" y="0.5" width="5" height="3"/></svg>
        (555)618-2047
      </span>
      <span class="contact__item">
        <svg viewBox="0 0 10 10"><rect x="0.5" y="1.5" width="9" height="7"/></svg>
        mtorvel@bhcpins.com
      </span>
    </div>
    <div class="contact contact--address">4287 Willowgate Pkwy, suite D Fairmont Springs, CA 91458</div>
    <div class="contact contact--licence">Lic.No : 0K52718</div>
  </section>

  <section class="card card--back-light">
    <div class="brand">
      <span class="brand__square"></span>
      <span class="brand__name">Bright Harbor<br>Coverage Partners</span>
    </div>
    <div class="back-rule"></div>
    <div class="back-band"></div>
  </section>

  <section class="card card--back-dark">
    <div class="brand brand--on-dark">
      <span class="brand__square"></span>
      <span class="brand__name">Bright Harbor<br>Coverage Partners</span>
    </div>
  </section>

</main>
</body>
</html>
```